Business Card Design Project

we need a business card design for our company: www.plomvik.ch
It's important to include our already existing logo (see website)

```html
<!DOCTYPE html>
<html lang="en">
<head>
<meta charset="utf-8">
<title>Plomvik – Business Card Design</title>
<link rel="stylesheet" href="https://fonts.googleapis.com/css2?family=Arimo:wght@400;700&display=swap">
<style>
  :root {
    --page-bg: #d9d9d9;
    --card-white: #ffffff;
    --brand-blue: #0a6fba;
    --brand-light: #7ea8dc;
    --label-ink: #1e1e1e;
    --card-shadow: rgba(0, 0, 0, 0.28);
  }
  * { margin: 0; padding: 0; box-sizing: border-box; }
  html, body { width: 1200px; height: 900px; overflow: hidden; }
  body {
    position: relative;
    background: var(--page-bg);
    font-family: "Arimo", Arial, sans-serif;
  }
  .option-label {
    position: absolute;
    left: 128px;
    font-size: 26px;
    color: var(--label-ink);
  }
  .option-label--one { top: 92px; }
  .option-label--two { top: 784px; }

  .card {
    position: absolute;
    width: 495px;
    height: 305px;
    border-radius: 16px;
    overflow: hidden;
    box-shadow: 0 6px 14px var(--card-shadow);
  }
  .card--front-white { left: 114px; top: 130px; background: var(--card-white); }
  .card--front-blue  { left: 114px; top: 455px; background: var(--brand-blue); }
  .card--back        { left: 640px; top: 300px; width: 500px; height: 310px; background: var(--card-white); }

  .wordmark {
    position: absolute;
    font-weight: 700;
    letter-spacing: -1px;
    line-height: 1;
  }
  .front-wordmark { left: 12px; top: 118px; font-size: 84px; }
  .card--front-white .front-wordmark { color: var(--brand-light); }
  .card--front-blue .front-wordmark { color: var(--card-white); }

  .front-url {
    position: absolute;
    left: 112px;
    top: 206px;
    font-size: 21px;
  }
  .card--front-white .front-url { color: var(--brand-blue); }
  .card--front-blue .front-url { color: var(--card-white); }

  .info-strip {
    position: absolute;
    left: 0;
    background: var(--brand-blue);
    color: var(--card-white);
    padding-left: 32px;
  }
  .info-strip--name    { top: 45px;  width: 228px; height: 64px; padding-top: 10px; }
  .info-strip--address { top: 125px; width: 222px; height: 70px; padding-top: 18px; font-size: 15px; line-height: 1.2; }
  .info-strip--contact { top: 212px; width: 215px; height: 68px; padding-top: 8px; padding-left: 30px; font-size: 15px; line-height: 1.2; }

  .person-name { font-size: 19px; font-weight: 700; }
  .person-role { font-size: 14px; margin-top: 3px; }

  .contact-line { display: flex; align-items: center; gap: 8px; }
  .contact-icon { width: 11px; height: 11px; flex: none; }

  .back-wordmark {
    left: 255px;
    top: 135px;
    font-size: 46px;
    color: var(--brand-light);
  }
</style>
</head>
<body>
  <p class="option-label option-label--one">Front Option 1</p>

  <section class="card card--front-white" aria-label="Card front, white option">
    <span class="wordmark front-wordmark">Plomvik</span>
    <span class="front-url">www.plomvik.ch</span>
  </section>

  <section class="card card--front-blue" aria-label="Card front, blue option">
    <span class="wordmark front-wordmark">Plomvik</span>
    <span class="front-url">www.plomvik.ch</span>
  </section>

  <p class="option-label option-label--two">Front Option 2</p>

  <section class="card card--back" aria-label="Card back">
    <div class="info-strip info-strip--name">
      <p class="person-name">Lena Brunner</p>
      <p class="person-role">Co-Founder</p>
    </div>
    <div class="info-strip info-strip--address">
      <p>Lindenweg 12</p>
      <p>8050 Zürich</p>
    </div>
    <div class="info-strip info-strip--contact">
      <p class="contact-line">
        <svg class="contact-icon" viewBox="0 0 12 12" aria-hidden="true"><path d="M2 1l2 0 1 3-1.2 1a6 6 0 0 0 3.2 3.2L8 7l3 1v2c0 .6-.5 1-1 1A9 9 0 0 1 1 2c0-.5.4-1 1-1z" fill="#fff"/></svg>
        <span>+41 44 310 47 86</span>
      </p>
      <p class="contact-line">
        <svg class="contact-icon" viewBox="0 0 12 12" aria-hidden="true"><rect x="0.5" y="2" width="11" height="8" rx="1" fill="#fff"/><path d="M1 2.5l5 4 5-4" fill="none" stroke="#0a6fba" stroke-width="1"/></svg>
        <span>info@plomvik.ch</span>
      </p>
      <p class="contact-line">
        <svg class="contact-icon" viewBox="0 0 12 12" aria-hidden="true"><circle cx="6" cy="6" r="5.3" fill="#fff"/><path d="M0.8 6h10.4M6 0.8c-2.5 2.8-2.5 7.6 0 10.4M6 0.8c2.5 2.8 2.5 7.6 0 10.4" fill="none" stroke="#0a6fba" stroke-width="0.8"/></svg>
        <span>plomvik.ch</span>
      </p>
    </div>
    <span class="wordmark back-wordmark">Plomvik</span>
  </section>
</body>
</html>
```